Soy Candle Business needs a label design

We need a label design for a new company selling soy candles - Velvet Hearth Co.

We are using apothecary jars in 3 sizes.
As per attached candles will be dressed with a beautiful black bow and all finished with a diamante in centre of bow.

We would like label done on lid of candle jars - 5cm circle (5cm from one side to the other), this way one label will fit each product size. Label will be done as a sticker.

We are thinking of the background colour to be black, however are open to recommendations. We want label to be classy, elegant and simple.

Inspiration for candle design came from attached invitation that features the bow, and beautiful vintage paper on top area.

Label should include the following 3 pieces of information:
Velvet Hearth Co (company name)
Coconut Lime (this will change depending on fragrance)
Soy Candle

Velvet Hearth Co does not have a company logo... what is done for the label will set tone for what is done across other elements of business moving forward.

Industry/Entity Type

Business

Requirements
Must have
• Velvet Hearth Co
Fragrance Flavour
Soy Candle

```html
<!DOCTYPE html>
<html lang="en">
<head>
<meta charset="utf-8">
<title>Velvet Hearth Co — Soy Candle Lid Labels</title>
<link rel="stylesheet" href="https://fonts.googleapis.com/css2?family=Dancing+Script:wght@500&family=Kaushan+Script&family=Cormorant+Garamond:wght@500&display=swap">
<style>
  :root {
    --page: #ffffff;
    --label-black: #14120f;
    --brand-yellow: #f3ee8e;
    --chocolate: #6a3d1c;
    --coconut-lime: #6bc3a0;
    --lavender: #b07fb8;
    --lavender-text: #8f55a3;
    --strawberry: #ee4e6c;
  }
  html, body {
    margin: 0;
    padding: 0;
    width: 1200px;
    height: 927px;
    overflow: hidden;
    background: var(--page);
  }
  .label-sheet { display: block; width: 1200px; height: 927px; }

  /* Accent colours are passed down through inheritance so they reach the shared label base */
  .label--chocolate    { --accent: var(--chocolate);    --accent-text: var(--chocolate); }
  .label--coconut-lime { --accent: var(--coconut-lime); --accent-text: var(--coconut-lime); }
  .label--lavender     { --accent: var(--lavender);     --accent-text: var(--lavender-text); }
  .label--strawberry   { --accent: var(--strawberry);   --accent-text: var(--strawberry); }

  .label-ring { fill: var(--accent); }
  .label-face { fill: var(--label-black); }
  .ornament { fill: var(--accent); opacity: 0.78; }

  .company-name {
    font-family: "Dancing Script", cursive;
    font-weight: 500;
    font-size: 30px;
    fill: var(--brand-yellow);
    letter-spacing: 0.5px;
  }
  .product-type {
    font-family: "Cormorant Garamond", serif;
    font-weight: 500;
    font-size: 22px;
    fill: var(--brand-yellow);
    letter-spacing: 0.5px;
  }
  .fragrance-name {
    font-family: "Kaushan Script", cursive;
    font-size: 52px;
    text-anchor: middle;
    fill: var(--accent-text);
  }
</style>
</head>
<body>
<svg class="label-sheet" viewBox="0 0 1200 927" xmlns="http://www.w3.org/2000/svg" role="img" aria-label="Velvet Hearth Co soy candle lid labels in four fragrances">
  <defs>
    <path id="arc-top" d="M -136 0 A 136 136 0 0 1 136 0"/>
    <path id="arc-bottom" d="M -126 0 A 126 126 0 0 0 126 0"/>
    <g id="label-base">
      <circle class="label-ring" r="172"/>
      <circle class="label-face" r="165"/>
      <path class="ornament" role="img" aria-label="Vintage flourish scrollwork, upper half" d="M -106.2 -24 A 108.8 108.8 0 0 1 106.2 -24 Z"/>
      <path class="ornament" role="img" aria-label="Vintage flourish scrollwork, lower half" d="M -103.4 34 A 108.8 108.8 0 0 0 103.4 34 Z"/>
      <text class="company-name"><textPath href="#arc-top" startOffset="50%" text-anchor="middle">Velvet Hearth Co</textPath></text>
      <text class="product-type"><textPath href="#arc-bottom" startOffset="50%" text-anchor="middle">SOY CANDLE</textPath></text>
    </g>
  </defs>

  <g class="label label--chocolate" transform="translate(347 253)">
    <use href="#label-base"/>
    <text class="fragrance-name" y="24">Chocolate</text>
  </g>

  <g class="label label--coconut-lime" transform="translate(868 251)">
    <use href="#label-base"/>
    <text class="fragrance-name" y="24">Coconut Lime</text>
  </g>

  <g class="label label--lavender" transform="translate(347 671)">
    <use href="#label-base"/>
    <text class="fragrance-name" y="24">Lavender</text>
  </g>

  <g class="label label--strawberry" transform="translate(868 667)">
    <use href="#label-base"/>
    <text class="fragrance-name" y="24">Strawberry</text>
  </g>
</svg>
</body>
</html>
```